INTERNATIONAL SPEAKING BUSINESS FOR WOMEN NEEDS A BROCHURE DESIGN

HEARTHSTONE CIRCLE IS AN INTERNATIONAL FEMALE NETWORK PROVIDING ITS MEMBERS THE UK'S NUMBER ONE RELATIONSHIP SEMINAR FOR WOMEN.
WE ARE ABOUT TO GO LIVE AGAIN AFTER 18 MONTHS AND ONE OF OUR OFFERINGS AT THIS LIVE EVENT, IS OUR BONDWISE WORKSHOP TRACK - AND THIS IS WHERE YOU COME IN :)
IM LOOKING FOR AN ELEGANT, EASY AND WARM TO THE EYE BROCHURE WHICH CAPTURES SOME OF OUR BEST TESTIMONIALS AND CLIENTS. WE HAVE THE LOGO, THE IMAGES AND THE COPY . WE JUST NEED YOUR AMAZING CREATIVE TALENT AND SKILL TO PUT IT ALL TOGETHER TO LOOK ELEGANT AND PROFESSIONAL, YET WELCOMING AND INSPIRING.
OUR IDEAL CLIENT IS A SINGLE, SUCCESSFUL, PROFESSIONAL WOMAN WANTING TO FIND A SOLUTION TO HER RELATIONSHIP CHALLENGES. SHE WANTS TO LET GO OF HER FEARS OF PAST RELATIONSHIPS AND ALIGN WITH AN AMAZING RELATIONSHIP. OUR AIM WITH THE BROCHURE IS TO SHOW THEM WHAT WE DO, HOW WE DO IT AND HOW OUR EXISTING CLIENTS HAVE ALREADY DONE THIS.
THIS IS JUST ONE OF MANY CREATIVE WORKS NEEDED TO BE CARRIED OUT OVER THESE NEXT FEW WEEKS
SO WE ARE LOOKING FOR OUR IDEAL CREATIVE PARTNER ! HOPING TO FIND YOU HERE ;)
hearthstonecircle-example.com
professional, successful women between 30 and 65 looking to resolve their relationship problems
Speaking Business/ Seminars / webinars/ Relationships Coaching for Women
- Similar to logo and website hearthstonecircle-example.com

```html
<!DOCTYPE html>
<html lang="en">
<head>
<meta charset="utf-8">
<title>Hearthstone Circle — Testimonials</title>
<link rel="stylesheet" href="https://fonts.googleapis.com/css2?family=Noto+Serif:wght@300;400&family=Zilla+Slab:wght@700&display=swap">
<style>
  :root {
    --rose: #e8436a;
    --ink: #2f2f33;
    --stone: #a6a7aa;
    --paper: #ffffff;
  }
  html, body { margin: 0; padding: 0; overflow: hidden; background: var(--paper); }
  .brochure-page {
    position: relative; width: 1200px; height: 856px; overflow: hidden;
    background: var(--paper); color: var(--ink);
    font-family: "Noto Serif", Georgia, serif; font-weight: 300;
  }
  .abs { position: absolute; }
  .client-name {
    margin: 0; font-family: "Zilla Slab", Georgia, serif; font-weight: 700;
    font-size: 15.5px; color: var(--rose); line-height: 1.2;
  }
  .client-role { margin: 0; font-size: 18.5px; line-height: 21.5px; font-weight: 400; }
  .quote { margin: 0; font-size: 18.5px; line-height: 23.7px; }
  .quote + .quote { margin-top: 12px; }
  .portrait { border-radius: 50%; width: 116px; height: 116px; }
  .portrait--empty { box-sizing: border-box; border: 1.5px solid #111; background: var(--paper); }
  .portrait--sabine { background: radial-gradient(circle at 50% 40%, #d9cfc6 0%, #b9b6b4 55%, #3a2f33 100%); }
  .portrait--delphine { background: radial-gradient(circle at 55% 40%, #e6cdb8 0%, #d8cabb 55%, #1c1a1b 100%); }
  .portrait--rosalind { background: radial-gradient(circle at 50% 45%, #5a3a40 0%, #2b2f3a 55%, #3d6f73 100%); }
  .brand {
    left: 833px; top: 330px; width: 290px;
    display: flex; flex-direction: column; align-items: flex-start; gap: 18px;
  }
  .brand-dot { width: 70px; height: 70px; border-radius: 50%; background: var(--rose); }
  .brand-name {
    margin: 0; font-family: "Noto Serif", Georgia, serif; font-weight: 400;
    font-size: 30px; line-height: 1.15; letter-spacing: 1px; color: var(--rose);
  }
  .footer-arcs { left: 0; top: 800px; }
</style>
</head>
<body>
<main class="brochure-page">

  <section class="testimonial">
    <div class="abs" style="left:63px;top:140px;">
      <h3 class="client-name">Harriet Lowell, 39</h3>
      <p class="client-role">Receptionist for<br>Adult Mental Health</p>
    </div>
    <div class="abs portrait portrait--empty" style="left:293px;top:113px;"></div>
    <div class="abs" style="left:63px;top:241px;width:350px;">
      <p class="quote">I feel incredibly lucky to have found this group of amazing women. The masterclass series and network has opened my eyes to how I treat myself, my thoughts, my emotions, and my mindset in general.</p>
    </div>
  </section>

  <section class="testimonial">
    <div class="abs" style="left:433px;top:140px;">
      <h3 class="client-name">Sabine Marchetti, 33</h3>
      <p class="client-role">Senior Customer Success<br>Manager</p>
    </div>
    <div class="abs portrait portrait--sabine" style="left:663px;top:113px;" role="img" aria-label="Portrait photo of Sabine Marchetti"></div>
    <div class="abs" style="left:433px;top:241px;width:350px;">
      <p class="quote">Masterclasses are like Mini mastery weekends, absolutely life changing.</p>
      <p class="quote">I’ve finally realised why I keep reliving patterns of behaviour like comparison, feeling worthless or stupid and it’s because I haven’t dealt with deep down emotions that I have learnt to suppress since I was young.</p>
    </div>
  </section>

  <section class="testimonial">
    <div class="abs portrait portrait--delphine" style="left:63px;top:432px;" role="img" aria-label="Portrait photo of Delphine"></div>
    <div class="abs" style="left:193px;top:469px;">
      <h3 class="client-name">Delphine, 42</h3>
      <p class="client-role">Hairstylist</p>
    </div>
    <div class="abs" style="left:63px;top:560px;width:350px;">
      <p class="quote">Masterclasses have been a fantastic way of consolidating Clara’s teaching in my mind after the weekends. It has been a great way to keep consistency in the tools which are disciplines that I very much need to shift my mindset.</p>
    </div>
  </section>

  <section class="testimonial">
    <div class="abs portrait portrait--rosalind" style="left:433px;top:489px;" role="img" aria-label="Portrait photo of Rosalind Ortega"></div>
    <div class="abs" style="left:563px;top:527px;">
      <h3 class="client-name">Rosalind Ortega, 38</h3>
      <p class="client-role">Director of Luxury Sales</p>
    </div>
    <div class="abs" style="left:433px;top:617px;width:350px;">
      <p class="quote">The Masterclass series is my most important weekly date with myself! They involve a deeper learning of all the tools. Having the chance to go through each of them in detail, allows me to engage in the benefit of practicing them each day.</p>
    </div>
  </section>

  <div class="abs brand">
    <span class="brand-dot" aria-hidden="true"></span>
    <p class="brand-name">HEARTHSTONE<br>CIRCLE</p>
  </div>

  <svg class="abs footer-arcs" width="1200" height="56" viewBox="0 0 1200 56" aria-hidden="true">
    <ellipse cx="380" cy="90" rx="330" ry="67" fill="var(--stone)"/>
    <ellipse cx="785" cy="90" rx="300" ry="67" fill="var(--rose)"/>
  </svg>

</main>
</body>
</html>
```